Personal Business Card

Looking for a clean and modern personal business card. Basically I need something catchy to give to potential clients and people I meet. I do a lot of freelancing (from DJ'ing to wedding videography, but its mostly on the event side of things) so it's more-so about selling myself rather than identifying with a company. I'm starting to meet more people that I want to work with after meeting them so I'm revamping my business cards.

I'm looking for a clean and modern design- I know that's really vague but I'm fine with anything ranging from a symbol to just a fancy version of my name.

Details I need on the front:
Dennis Kowal
dennis@denniskowal-mail.net
(555) 807-2291

On the back I'd like to have something simple like "Nice to have met you today" or "Great meeting you".

UPDATE 9/27 Noon: My apologies for not putting it up before- I'm definitely looking for full color. Doesn't have to be a rainbow but I am looking for the least amount of blank white as possible.

UPDATE 10/1: Really impressed with what I've been getting so far and I'm working on giving everyone feedback- if your design is still up then you're still in the run. Looking for something more unique and modern so please do not post something that looks like a template from Cardloom!

Target Market(s)

Mainly to give to people aged 18-35. Most of my encounters will be casual so the card should have a "young" feeling to it. I rarely do anything in the corporate world so it doesn't have to be boring. It should give the impression that I'm the one they should go to if they need what I do (again it changes every weekend so I'll probably say the "what I do" part.

Industry/Entity Type

Wedding

Requirements
Must have
• Basically the contact information listed above
Nice to have
• I really like the colors Blue, Silver, and Purple. They don't have to necessarily all be there though. I do like the look of polished metal if that makes sense.
Should not have
• A template that resembles card-loom. I'm in a point in my life where I'm working a lot of different markets/areas so the card does not need to have an address or address placeholder.

```html
<!DOCTYPE html>
<html lang="en">
<head>
<meta charset="utf-8">
<title>DJ Dennis Kowal – Business Card</title>
<link href="https://fonts.googleapis.com/css2?family=Arimo:wght@400;700&display=swap" rel="stylesheet">
<style>
  :root {
    --stage: #9a9a9e;
    --card-white: #ffffff;
    --ink-blue: #101080;
    --violet: #5a18c8;
    --silver: #d8d8dc;
    --line-dark: #0b0b1e;
  }
  * { margin: 0; padding: 0; box-sizing: border-box; }
  html, body {
    width: 1200px; height: 900px; overflow: hidden;
    background: var(--stage);
    font-family: "Arimo", Arial, sans-serif;
  }
  .canvas { position: relative; width: 1200px; height: 900px; }
  .card {
    position: absolute; width: 700px; height: 400px; overflow: hidden;
    background: var(--card-white);
    border: 2px solid var(--ink-blue);
  }
  .card svg { position: absolute; inset: 0; }
  .card-front { left: 60px; top: 50px; }
  .card-back { left: 440px; top: 470px; }

  .name {
    position: absolute; left: 118px; top: 70px;
    font-size: 50px; font-weight: 700; color: var(--ink-blue);
    letter-spacing: 0.5px; transform: rotate(-6deg); transform-origin: left center;
    white-space: nowrap;
  }
  .contact {
    position: absolute; left: 440px; top: 240px;
    list-style: none; color: var(--card-white); font-weight: 700;
    transform: rotate(-6deg); transform-origin: left center;
  }
  .contact li { display: flex; align-items: center; gap: 12px; margin-bottom: 10px; white-space: nowrap; }
  .contact .phone { font-size: 22px; }
  .contact .email { font-size: 15px; }
  .contact .dot {
    width: 24px; height: 24px; border-radius: 50%; flex: none;
    background: radial-gradient(circle at 35% 35%, #8fb8ff, #2a5fd8 70%);
    border: 1px solid var(--silver);
  }
  .greeting {
    position: absolute; left: 100px; top: 222px;
    font-size: 36px; line-height: 42px; font-weight: 700; color: var(--violet);
    transform: rotate(-12deg); transform-origin: left center;
    white-space: nowrap;
  }
</style>
</head>
<body>
<main class="canvas">

  <section class="card card-front" aria-label="Business card front">
    <svg width="700" height="400" viewBox="0 0 700 400" aria-hidden="true">
      <defs>
        <linearGradient id="front-sky" x1="0" y1="0" x2="0" y2="1">
          <stop offset="0" stop-color="#ffffff"/>
          <stop offset="1" stop-color="#eeeee6"/>
        </linearGradient>
        <radialGradient id="front-blue" cx="0.35" cy="0.35" r="0.8">
          <stop offset="0" stop-color="#2a2aff"/>
          <stop offset="0.55" stop-color="#1010b0"/>
          <stop offset="1" stop-color="#04043a"/>
        </radialGradient>
        <linearGradient id="front-fade" x1="0" y1="0" x2="0" y2="1">
          <stop offset="0" stop-color="#ffffff" stop-opacity="0.9"/>
          <stop offset="1" stop-color="#ffffff" stop-opacity="0"/>
        </linearGradient>
        <linearGradient id="ring-metal" x1="0" y1="0" x2="1" y2="1">
          <stop offset="0" stop-color="#ffffff"/>
          <stop offset="0.4" stop-color="#8a8a92"/>
          <stop offset="0.7" stop-color="#f0f0f4"/>
          <stop offset="1" stop-color="#5a5a62"/>
        </linearGradient>
      </defs>
      <rect class="front-base" width="700" height="400" fill="url(#front-sky)"/>
      <path class="front-sweep" d="M0,250 C160,140 360,250 700,150 L700,400 L0,400 Z" fill="url(#front-blue)"/>
      <path class="front-haze" d="M0,250 C160,140 360,250 700,150 L700,215 C380,300 170,210 0,300 Z" fill="url(#front-fade)"/>
      <path class="front-edge" d="M0,250 C160,140 360,250 700,150" fill="none" stroke="var(--line-dark)" stroke-width="5"/>
      <path class="front-edge-shine" d="M0,256 C160,146 360,256 700,156" fill="none" stroke="var(--silver)" stroke-width="2"/>
      <ellipse class="front-ring" cx="170" cy="300" rx="118" ry="62" transform="rotate(-8 170 300)" fill="none" stroke="url(#ring-metal)" stroke-width="9"/>
    </svg>
    <h1 class="name">DJ Dennis Kowal</h1>
    <ul class="contact">
      <li class="phone"><span class="dot"></span>(555) 807-2291</li>
      <li class="email"><span class="dot"></span>dennis@denniskowal-mail.net</li>
    </ul>
  </section>

  <section class="card card-back" aria-label="Business card back">
    <svg width="700" height="400" viewBox="0 0 700 400" aria-hidden="true">
      <defs>
        <linearGradient id="back-deep" x1="0.2" y1="0.1" x2="0.7" y2="1">
          <stop offset="0" stop-color="#ffffff" stop-opacity="0"/>
          <stop offset="0.35" stop-color="#6a6af0"/>
          <stop offset="0.65" stop-color="#1a1ad0"/>
          <stop offset="1" stop-color="#05054a"/>
        </linearGradient>
        <linearGradient id="back-top" x1="0" y1="0.6" x2="1" y2="0">
          <stop offset="0" stop-color="#ffffff" stop-opacity="0"/>
          <stop offset="0.5" stop-color="#5a5aff"/>
          <stop offset="1" stop-color="#08086a"/>
        </linearGradient>
        <linearGradient id="back-ring-metal" x1="0" y1="0" x2="1" y2="1">
          <stop offset="0" stop-color="#ffffff"/>
          <stop offset="0.45" stop-color="#7a7a84"/>
          <stop offset="0.75" stop-color="#f4f4f8"/>
          <stop offset="1" stop-color="#4a4a52"/>
        </linearGradient>
      </defs>
      <rect class="back-base" width="700" height="400" fill="var(--card-white)"/>
      <path class="back-crest" d="M380,120 C480,80 580,62 700,60 L700,0 L520,0 C480,50 440,90 380,120 Z" fill="url(#back-top)"/>
      <path class="back-sweep" d="M0,400 L700,400 L700,170 C560,300 300,330 120,400 Z" fill="url(#back-deep)"/>
      <path class="back-wave" d="M0,200 C200,190 400,110 700,60" fill="none" stroke="var(--line-dark)" stroke-width="5"/>
      <ellipse class="back-ring" cx="150" cy="330" rx="115" ry="55" transform="rotate(-12 150 330)" fill="none" stroke="url(#back-ring-metal)" stroke-width="9"/>
    </svg>
    <p class="greeting">Nice to have met you today.</p>
  </section>

</main>
</body>
</html>
```